Stationary Design for Norvack Digital

We are after a full stationary back business cards, letterheads, compliment slip, invoice template, delivery note and anything else we could use within the stationary pack.

We would also like an email footer creating.

Our company details to be included on all stationary:

Registered Name: Norvack Limited
Company Registration Number: 20483957
Website: www.norvackdigital.example
email: info@norvackdigital.example
Phone: 01632 960 417
Address: 48 Elmstead Lane Loughborough Leicestershire United Kingdom LE14 7QW

Industry/Entity Type

Business

```html
<!DOCTYPE html>
<html lang="en">
<head>
<meta charset="utf-8">
<title>Norvack Digital – Stationery Pack</title>
<link href="https://fonts.googleapis.com/css2?family=Arimo:wght@400;700&family=Open+Sans:wght@400&display=swap" rel="stylesheet">
<style>
  :root {
    --navy: #0e3166;
    --sheet-grey: #cfd0d2;
    --swoosh-light: #e4e5e7;
    --swoosh-dark: #a9abae;
    --paper: #ffffff;
    --ink: #4a4a4a;
    --label: #7a7a7a;
    --bg-centre: #fbfbfb;
    --bg-edge: #e2e2e2;
  }
  * { margin: 0; padding: 0; box-sizing: border-box; }
  html, body { width: 923px; height: 1200px; overflow: hidden; }
  body {
    position: relative;
    background: radial-gradient(ellipse at 50% 45%, var(--bg-centre) 0%, var(--bg-edge) 100%);
    font-family: "Arimo", Arial, sans-serif;
  }
  .piece {
    position: absolute;
    background: var(--paper);
    box-shadow: 2px 3px 4px rgba(0,0,0,0.35);
    overflow: hidden;
  }
  .piece--grey { background: var(--sheet-grey); }
  .swoosh { position: absolute; left: 0; top: 0; width: 100%; height: 100%; }
  .brand-name {
    position: absolute;
    font-family: "Arimo", Arial, sans-serif;
    font-weight: 700;
    color: var(--navy);
    white-space: nowrap;
    letter-spacing: 0.5px;
  }
  .brand-name--reverse { color: var(--paper); left: 0; width: 100%; text-align: center; }
  .web-url {
    position: absolute; left: 0; width: 100%; text-align: center;
    color: var(--paper); font-size: 8.5px;
  }
  .footer-details {
    position: absolute; left: 0; width: 100%; text-align: center;
    color: var(--paper); font-size: 7.6px; line-height: 11.5px;
  }
  .letter-body {
    position: absolute; left: 43px; top: 156px; width: 348px;
    font-family: "Open Sans", Arial, sans-serif;
    font-size: 5.9px; line-height: 10.3px; color: var(--ink);
  }
  .letter-body p { margin-bottom: 10.3px; }
  .signature-line {
    position: absolute; left: 43px; top: 442px;
    font-size: 8px; color: var(--ink);
  }
  .item-label {
    position: absolute; font-size: 17px; color: var(--label);
    transform: translateX(-50%); letter-spacing: 0.5px;
  }
  .card-person {
    position: absolute; left: 10px; top: 140px; width: 105px; text-align: right;
    color: var(--paper);
  }
  .card-person__name { font-size: 12.5px; line-height: 14px; }
  .card-person__role { font-size: 9.5px; letter-spacing: 1px; }
  .card-divider {
    position: absolute; left: 122px; top: 124px; width: 1px; height: 62px;
    background: var(--paper);
  }
  .card-contact {
    position: absolute; left: 133px; top: 121px;
    color: var(--paper); font-size: 8.5px; line-height: 10.5px;
  }
  .card-contact__gap { height: 8px; }
</style>
</head>
<body>

  <!-- Letterhead -->
  <section class="piece letterhead" style="left:20px; top:53px; width:430px; height:607px;">
    <div class="brand-name" style="left:22px; top:28px; font-size:17px;">Norvack Digital</div>
    <div class="letter-body">
      <p>Thank you for your recent enquiry about our digital services. We are pleased to confirm the details of the proposal discussed at our meeting last week, including the project scope, delivery stages and agreed budget. Please review the attached summary and let us know if any part needs further clarification before work begins.</p>
      <p>Our team will begin with a short discovery phase to understand your goals, audience and existing materials. From there we will prepare design concepts, gather your feedback and refine the chosen direction across print and digital formats. Each stage will be shared for approval, and we will keep you updated on progress through regular calls and written reports so that nothing is missed along the way.</p>
      <p>Invoices will be issued at the start and completion of the project. Payment terms are thirty days from the invoice date, and all prices quoted are exclusive of VAT. Any additional work outside the agreed scope will be estimated separately.</p>
      <p>We look forward to working with you on this project. If you have any questions in the meantime, please contact our office by phone or email and a member of the team will be happy to help.</p>
    </div>
    <div class="signature-line">Signature ....................................</div>
    <svg class="swoosh" viewBox="0 0 466 658" preserveAspectRatio="none" aria-hidden="true">
      <defs>
        <linearGradient id="lhGrey" x1="0" y1="0" x2="1" y2="0">
          <stop offset="0" stop-color="var(--swoosh-light)"/>
          <stop offset="1" stop-color="var(--swoosh-dark)"/>
        </linearGradient>
      </defs>
      <path d="M0 540 Q 250 625 466 510 L466 658 L0 658 Z" fill="url(#lhGrey)"/>
      <path d="M0 566 Q 250 618 466 545 L466 658 L0 658 Z" fill="var(--navy)"/>
    </svg>
    <div class="footer-details" style="top:563px;">
      NORVACK LIMITED<br>
      48 Elmstead Lane Loughborough Leics LE14 7QW | Company Reg: 20483957 VAT Number:<br>
      P: 01632 960 417 &nbsp;|&nbsp; E: info@norvackdigital.example &nbsp;|&nbsp; W: www.norvackdigital.example
    </div>
  </section>

  <!-- Letterhead reverse -->
  <section class="piece piece--grey letterhead-back" style="left:472px; top:54px; width:429px; height:607px;">
    <div class="brand-name brand-name--reverse" style="top:300px; font-size:40px;">Norvack Digital</div>
    <div class="web-url" style="top:577px;">www.norvackdigital.example</div>
  </section>

  <div class="item-label" style="left:236px; top:688px;">Envelope</div>
  <div class="item-label" style="left:684px; top:692px;">Slip</div>

  <!-- Envelope -->
  <section class="piece envelope" style="left:27px; top:732px; width:425px; height:188px;">
    <div class="brand-name" style="left:15px; top:22px; font-size:14px;">Norvack Digital</div>
    <svg class="swoosh" viewBox="0 0 460 204" preserveAspectRatio="none" aria-hidden="true">
      <defs>
        <linearGradient id="envGrey" x1="0" y1="0" x2="1" y2="0">
          <stop offset="0" stop-color="var(--swoosh-light)"/>
          <stop offset="1" stop-color="var(--swoosh-dark)"/>
        </linearGradient>
      </defs>
      <path d="M0 108 Q 240 160 460 62 L460 204 L0 204 Z" fill="url(#envGrey)"/>
      <path d="M0 120 Q 240 168 460 92 L460 204 L0 204 Z" fill="var(--navy)"/>
    </svg>
    <div class="footer-details" style="top:150px; font-size:7.4px; line-height:11px;">
      NORVACK LIMITED<br>
      48 Elmstead Lane Loughborough Leics LE14 7QW | Company Reg: 20483957 VAT Number:<br>
      P: 01632 960 417 &nbsp;|&nbsp; E: info@norvackdigital.example &nbsp;|&nbsp; W: www.norvackdigital.example
    </div>
  </section>

  <!-- Compliment slip -->
  <section class="piece piece--grey compliment-slip" style="left:475px; top:733px; width:423px; height:187px;">
    <div class="brand-name brand-name--reverse" style="top:74px; font-size:30px;">Norvack Digital</div>
    <div class="web-url" style="top:166px; font-size:8px;">www.norvackdigital.example</div>
  </section>

  <!-- Business card front -->
  <section class="piece business-card" style="left:112px; top:952px; width:340px; height:193px;">
    <div class="brand-name" style="left:14px; top:20px; font-size:14px;">Norvack Digital</div>
    <svg class="swoosh" viewBox="0 0 368 209" preserveAspectRatio="none" aria-hidden="true">
      <defs>
        <linearGradient id="cardGrey" x1="0" y1="0" x2="1" y2="0">
          <stop offset="0" stop-color="var(--swoosh-light)"/>
          <stop offset="1" stop-color="var(--swoosh-dark)"/>
        </linearGradient>
      </defs>
      <path d="M0 72 Q 190 135 368 40 L368 209 L0 209 Z" fill="url(#cardGrey)"/>
      <path d="M0 85 Q 190 142 368 62 L368 209 L0 209 Z" fill="var(--navy)"/>
    </svg>
    <div class="card-person">
      <div class="card-person__name">PERSON NAME</div>
      <div class="card-person__role">Designation</div>
    </div>
    <div class="card-divider"></div>
    <div class="card-contact">
      48 Elmstead Lane Loughborough Leics<br>
      LE14 7QW
      <div class="card-contact__gap"></div>
      P: 01632 960 417<br>
      E: info@norvackdigital.example<br>
      W: www.norvackdigital.example
    </div>
  </section>

  <!-- Business card back -->
  <section class="piece piece--grey business-card-back" style="left:474px; top:952px; width:340px; height:193px;">
    <div class="brand-name brand-name--reverse" style="top:82px; font-size:26px;">Norvack Digital</div>
    <div class="web-url" style="top:158px; font-size:8px;">www.norvackdigital.example</div>
  </section>

</body>
</html>
```